Ledgerwise Reach - B2B Demand Generation Website Project

We need a fully functional website for www.ledgerwisereach.example. We are a B2B Demand Generation company, based in London, working with companies such as QRT, VKD, Norvex, Brindlow, Tarvo generating them sales leads for their sales teams. We run this through digital marketing newsletter promotions and have a network of websites. Content syndication, data, demand generation, online marketing. Our logo has just been redone (attached) and we have a holding page already which i would like to use the style / colours. Our logo is bright and vibrant but i dont want the site to be a rainbow. We are expensive, classy, professorial, B2B, intelligent.

Home
About Us
Our Services
Prospora & QA Technology
Intent Data
Testimonials
Contact Us
Updates

Target Market(s)

B2B Marketers (QRT, Velquarion, Tarvo, VKD, Opal Reach, Driftmoor, Harlow Quantis, Technology Companies, Data Companies, Marketing Teams, Tumbleden.

Industry/Entity Type

Marketing

Coding

Coded - Design and coding required

Number of Pages Required

5+ page

Font styles to use
Sans Serif

Requirements
Must have
• Home
About Us
Our Services
Prospora & QA Technology
Intent Data
Testimonials
Contact Us

Simple Pages.

Look classy, intelligent, data experts. I like the video homepages were the image moves at the top. Very soft animation.
Nice to have
• Websites i like:

https://www.vkd.example/
https://www.brevantor.example/
https://www.plumfieldsites.example.co.uk/

Ledgerwise Reach - The Demand Generation Company
Should not have
• Glimpsevault crap images

```html
<!DOCTYPE html>
<html lang="en">
<head>
<meta charset="utf-8">
<title>Ledgerwise Reach - The Demand Generation Company</title>
<link rel="stylesheet" href="https://fonts.googleapis.com/css2?family=Exo+2:wght@300;400;500&family=Montserrat:wght@400;500;600;700&display=swap">
<style>
:root{
  --red:#c0272d;
  --red-soft:#e39a9a;
  --blue:#1f4c97;
  --hero:#2f4b88;
  --hero-deep:#22386b;
  --ink:#2b2b2b;
  --muted:#555;
  --grey-bg:#f2f2f2;
  --line:#d4d4d4;
  --footer:#15233a;
  --footer-text:#c9cfdb;
  --white:#fff;
}
*{margin:0;padding:0;box-sizing:border-box}
html,body{width:1200px;height:4305px;overflow:hidden}
body{position:relative;background:var(--white);font-family:"Montserrat",sans-serif;color:var(--ink)}
.abs{position:absolute}
.head{font-family:"Exo 2",sans-serif;font-weight:400;color:var(--blue)}
.eyebrow{font-family:"Exo 2",sans-serif;font-size:19px;letter-spacing:1px;color:var(--red);text-transform:uppercase;font-weight:400}
.btn{position:absolute;height:37px;border-radius:19px;background:var(--red);color:var(--white);font-size:10px;font-weight:700;letter-spacing:1.4px;display:flex;align-items:center;justify-content:center;gap:8px;text-transform:uppercase}
.btn svg{width:16px;height:8px}
.btn.ghost{background:var(--white);color:var(--red);border:2px solid var(--white)}
.para{font-size:11.5px;line-height:18.6px;color:#444;letter-spacing:.6px;text-align:justify}
.para p+p{margin-top:6px}
.para b{font-weight:700;color:#222}

/* hero */
.hero{left:0;top:0;width:1200px;height:605px;overflow:hidden;background:linear-gradient(120deg,#3a5794 0%,var(--hero) 45%,var(--hero-deep) 100%)}
.hero-photo{left:0;top:0;width:1200px;height:605px;background:radial-gradient(ellipse 420px 300px at 560px 260px,rgba(120,140,190,.45),transparent 70%),radial-gradient(ellipse 300px 260px at 250px 380px,rgba(20,30,60,.35),transparent 70%)}
.hero-curve{left:0;top:440px}
.brand{left:159px;top:22px;width:182px;text-align:center;color:var(--white)}
.brand-mark{width:40px;height:40px;border-radius:50%;border:2px solid var(--white);margin:0 auto 6px}
.brand-name{font-family:"Exo 2",sans-serif;font-size:26px;font-weight:300;letter-spacing:-.3px;line-height:28px}
.brand-tag{font-size:7px;margin-top:3px;letter-spacing:.3px}
.menu{left:1013px;top:36px;width:27px}
.menu span{display:block;height:2px;background:var(--white);margin-bottom:7px}
.play{left:578px;top:294px;width:40px;height:40px;border-radius:50%;background:rgba(255,255,255,.55);display:flex;align-items:center;justify-content:center}
.hero-copy{right:164px;top:190px;text-align:right}
.hero-copy .eyebrow{font-size:21px}
.hero-title{font-family:"Exo 2",sans-serif;font-size:32px;line-height:37px;color:var(--white);font-weight:400;margin-top:8px}

/* about */
.about-head{left:163px;top:688px;font-size:29px;line-height:35px}
.about-text{left:163px;top:815px;width:364px}
.stat{border:1.5px solid var(--red-soft);text-align:center;display:flex;flex-direction:column;align-items:center;justify-content:center}
.stat-num{font-size:30px;font-weight:700;color:#111;letter-spacing:1px}
.stat-num sup{font-size:17px;vertical-align:6px}
.stat-rule{width:20px;height:1px;background:#999;margin:14px 0 12px}
.stat-label{font-size:16px;line-height:23px;color:#222}

/* services */
.band{left:0;width:1200px;background:var(--grey-bg)}
.section-head{font-size:29px;line-height:35px}
.card{background:var(--white);border:1.5px solid #bdbdbd;box-shadow:0 3px 8px rgba(0,0,0,.12);padding:68px 25px 0}
.card.active{border:2px solid var(--red);box-shadow:none}
.card h3{font-family:"Montserrat",sans-serif;font-weight:500;font-size:16.5px;line-height:21px;color:#222}
.card.active h3{color:var(--red)}
.card p{margin-top:30px;font-size:9.2px;line-height:18.8px;color:#333;text-align:justify}
.card .more{position:absolute;right:25px;top:270px;font-size:9.5px;color:#333}
.card.active .more{color:var(--red)}

/* qa */
.laptop{left:92px;top:1988px;width:538px;height:293px;background:linear-gradient(180deg,#e8ebf0 0%,#cfd4dc 80%,#9aa0a8 100%);border-radius:14px 14px 4px 4px}
.qa-head{left:668px;top:1984px;font-size:29px;line-height:34px}
.qa-text{left:668px;top:2074px;width:373px}

/* intent */
.cubes{left:643px;top:2582px;width:443px;height:317px;background:radial-gradient(ellipse 180px 130px at 50% 50%,rgba(64,224,224,.75),rgba(128,140,240,.35) 60%,transparent 75%)}
.intent-head{left:160px;top:2533px;font-size:29px;line-height:34.5px}
.intent-text{left:160px;top:2662px;width:368px}

/* testimonials */
.center{left:0;width:1200px;text-align:center}
.tcard{border:1.5px solid var(--red-soft);box-shadow:0 2px 6px rgba(0,0,0,.06);background:var(--white);width:356px;height:161px;top:3285px;padding:60px 25px 0}
.avatar{width:57px;height:57px;border-radius:50%;background:#d6d6d6;position:absolute;left:24px;top:-30px}
.quote{position:absolute;right:24px;top:28px;color:var(--red);font-family:"Exo 2",sans-serif;font-size:58px;font-weight:500;line-height:58px}
.tname{font-size:11px;font-weight:700;color:#222}
.tname span{font-weight:400;font-size:9px;color:#555}
.tcard p{margin-top:14px;font-size:9.3px;line-height:15.6px;color:#444}
.dots{display:flex;gap:6px;justify-content:center}
.dots i{width:9px;height:9px;border-radius:50%;background:#9a9a9a;display:block}
.dots i.on{background:var(--red)}

/* partners */
.partner{top:3788px;width:180px;text-align:center;font-family:"Montserrat",sans-serif;font-weight:700;font-size:40px;color:#1f3f9a;letter-spacing:2px}

/* footer */
.footer{left:0;top:3959px;width:1200px;height:346px;background:var(--footer);color:var(--footer-text)}
.fcol{position:absolute;top:43px}
.fcol h4{font-size:10px;font-weight:700;color:var(--white);letter-spacing:.6px;margin-bottom:28px}
.fcol li{list-style:none;font-size:9.5px;line-height:20.5px}
.fcol.company li{line-height:17.5px}
.fsmall{font-size:9.5px;line-height:16px}
.fred{color:#e0474d;font-size:8.5px;font-weight:600;letter-spacing:1px;margin-top:8px}
.subscribe{margin-top:26px}
.email-box{margin-top:14px;width:219px;height:31px;border:1px solid #8f99ab;display:flex;align-items:center;justify-content:space-between;padding:0 10px;font-size:9px}
.email-box b{color:#e0474d;font-size:8.5px;font-weight:600}
.contact li{display:flex;gap:8px;align-items:center;line-height:16px;margin-bottom:15px}
.contact svg{width:11px;height:11px;flex:none}
.copy{left:160px;top:313px;font-size:9px}
.social{left:955px;top:306px;display:flex;gap:10px}
.social i{width:21px;height:21px;border-radius:50%;border:1.5px solid var(--white);display:block}
.social i.r{border-color:#e0474d}
</style>
</head>
<body>

<!-- HERO -->
<section class="abs hero">
  <div class="abs hero-photo" role="img" aria-label="Photograph of a business person reviewing charts on a tablet, tinted deep blue"></div>
  <div class="abs brand">
    <div class="brand-mark"></div>
    <div class="brand-name">ledgerwisereach</div>
    <div class="brand-tag">The Demand Generation Company</div>
  </div>
  <div class="abs menu"><span></span><span></span><span></span></div>
  <div class="abs play"><svg width="14" height="14" viewBox="0 0 14 14"><path d="M4 2 L12 7 L4 12 Z" fill="#2f4b88"/></svg></div>
  <div class="abs hero-copy">
    <div class="eyebrow">Ledgerwise Reach —</div>
    <div class="hero-title">The Demand Generation<br>Company</div>
  </div>
  <div class="btn" style="left:732px;top:358px;width:142px">About us <svg viewBox="0 0 16 8"><path d="M0 4H14M10 1L14 4L10 7" stroke="currentColor" stroke-width="1.3" fill="none"/></svg></div>
  <div class="btn ghost" style="left:894px;top:358px;width:144px">Services <svg viewBox="0 0 16 8"><path d="M0 4H14M10 1L14 4L10 7" stroke="currentColor" stroke-width="1.3" fill="none"/></svg></div>
  <svg class="abs hero-curve" width="1200" height="165" viewBox="0 0 1200 165"><path d="M0 165 C 400 145 800 110 1200 40 L1200 165 Z" fill="#fff"/></svg>
</section>

<!-- ABOUT -->
<div class="abs eyebrow" style="left:163px;top:655px">— About us</div>
<h1 class="abs head about-head">Ledgerwise Reach<br>The Demand Generation<br>Company</h1>
<div class="abs para about-text">
  <p><b>Ledgerwise Reach</b> offers multi-channel demand generation services to publishers and technology vendors through our network of lead generation websites and native speaking telemarketing agents.</p>
  <p>Whether looking for MQL, ABM or BANT campaigns, <b>Ledgerwise Reach</b> can assist you in delivering your demand generation strategy and generate pipeline for your sales teams and/or channel partners.</p>
</div>
<div class="btn" style="left:391px;top:1013px;width:136px">About us <svg viewBox="0 0 16 8"><path d="M0 4H14M10 1L14 4L10 7" stroke="currentColor" stroke-width="1.3" fill="none"/></svg></div>

<div class="abs stat" style="left:590px;top:692px;width:209px;height:166px">
  <div class="stat-num">70,000<sup>+</sup></div><div class="stat-rule"></div><div class="stat-label">Downloads Per<br>Month</div>
</div>
<div class="abs stat" style="left:831px;top:692px;width:209px;height:166px">
  <div class="stat-num">25,000<sup>+</sup></div><div class="stat-rule"></div><div class="stat-label">Leads Delivered<br>Per Month</div>
</div>
<div class="abs stat" style="left:590px;top:882px;width:450px;height:167px">
  <div class="stat-num">50<sup>+</sup></div><div class="stat-rule"></div><div class="stat-label">Countries We Can<br>Reach</div>
</div>

<!-- SERVICES -->
<section class="abs band" style="top:1141px;height:719px">
  <div class="abs eyebrow" style="left:163px;top:67px">— Our services</div>
  <h2 class="abs head section-head" style="left:163px;top:94px">What We’re Great At</h2>

  <div class="abs card active" style="left:160px;top:194px;width:248px;height:356px">
    <h3>Marketing Qualified<br>Leads (MQL)</h3>
    <p>A Marketing Qualified Lead (MQL) is a prospect that has expressed an interest in what your brand has to offer. An MQL has taken the first steps to becoming a customer and is ready to receive ...</p>
    <span class="more">Continue ›</span>
  </div>
  <div class="abs card" style="left:486px;top:194px;width:248px;height:356px">
    <h3>Account Based Marketing<br>Leads (ABM)</h3>
    <p>ABM is a strategy that directs marketing resources to engaging a specific set of target accounts.<br>Instead of casting a wide net to engage any potential customers...</p>
    <span class="more">Continue ›</span>
  </div>
  <div class="abs card" style="left:792px;top:194px;width:248px;height:356px">
    <h3>Sales Qualified Lead<br>/ BANT</h3>
    <p>An SQL lead or a BANT lead is a type of lead that expressed a specific interest in a product and service that you have to offer...<br>The difference between marketing qualified leads (MQL) and sales ...</p>
    <span class="more">Continue ›</span>
  </div>

  <div class="btn" style="left:531px;top:612px;width:136px">View services <svg viewBox="0 0 16 8"><path d="M0 4H14M10 1L14 4L10 7" stroke="currentColor" stroke-width="1.3" fill="none"/></svg></div>
</section>

<!-- QA TECHNOLOGY -->
<div class="abs laptop" role="img" aria-label="Laptop showing the Prospora project dashboard with candidate cards and filters"></div>
<div class="abs eyebrow" style="left:668px;top:1956px">— QA Technology</div>
<h2 class="abs head qa-head">Prospora : Verification<br>Platform from Ledgerwise Reach</h2>
<div class="abs para qa-text">
  <p>Prospora is a proprietary lead verification platform from Ledgerwise Reach that aims to sift out invalid leads with questionable or erroneous data. The platform is designed to equip sales teams with accurate, high-quality records in order to improve lead generation, accelerate pipeline and increase revenue.</p>
  <p>Prospora is positioned to quickly identify, validate, and improve lead quality at the point-of-entry by filtering out all leads that do not match required filters, such as job title, company size, etc.</p>
</div>
<div class="btn" style="left:907px;top:2283px;width:136px">Discover <svg viewBox="0 0 16 8"><path d="M0 4H14M10 1L14 4L10 7" stroke="currentColor" stroke-width="1.3" fill="none"/></svg></div>

<!-- INTENT DATA -->
<section class="abs band" style="top:2420px;height:601px"></section>
<div class="abs eyebrow" style="left:160px;top:2504px">— Intent data</div>
<h2 class="abs head intent-head">Access To 35 Million<br>Individuals And a Global<br>Behavioural Data Stream</h2>
<div class="abs para intent-text">
  <p>Our relationships with the world’s most important technology &amp; business decisions-makers generate a perpetual stream of global data. With access to 35 million individuals and a global behavioural data stream that is authenticated, timely and contextually relevant, we have one of the industry’s most powerful signals of buyer intent and can fuel your demand-generation marketing strategies globally.</p>
  <p>We support our Intent targeting capabilities by partnering with a number of third party intent providers, meaning we are able to target the global data universe to deliver the best and most engaging leads to our partners.</p>
</div>
<div class="btn" style="left:398px;top:2896px;width:135px">More details <svg viewBox="0 0 16 8"><path d="M0 4H14M10 1L14 4L10 7" stroke="currentColor" stroke-width="1.3" fill="none"/></svg></div>
<div class="abs cubes" role="img" aria-label="Isometric illustration of glowing cyan data cubes on a layered platform"></div>

<!-- TESTIMONIALS -->
<div class="abs center eyebrow" style="top:3106px">— Testimonials —</div>
<h2 class="abs center head section-head" style="top:3135px">What our Clients Says<br>About Us</h2>

<div class="abs tcard" style="left:159px">
  <div class="avatar"></div><div class="quote">”</div>
  <div class="tname">Marcus Hale <span>/ CEO QRT</span></div>
  <p>Lorem ipsum dolor sit amet, consectetur adipiscing elit. Donec ut sem elementum, tristique justo quis, varius risus. Vivamus consectetur sapien sodales arcu interdum, at dapibus mi porta.</p>
</div>
<div class="abs tcard" style="left:685px">
  <div class="avatar"></div><div class="quote">”</div>
  <div class="tname">Marcus Hale <span>/ CEO QRT</span></div>
  <p>Lorem ipsum dolor sit amet, consectetur adipiscing elit. Donec ut sem elementum, tristique justo quis, varius risus. Vivamus consectetur sapien sodales arcu interdum, at dapibus mi porta.</p>
</div>
<div class="abs center dots" style="top:3490px"><i></i><i class="on"></i><i></i></div>

<!-- PARTNERS -->
<section class="abs band" style="top:3589px;height:370px"></section>
<div class="abs center eyebrow" style="top:3639px">— Who we work with —</div>
<h2 class="abs center head section-head" style="top:3668px">People Who Trust Us</h2>
<div class="abs partner" style="left:160px">QRT</div>
<div class="abs partner" style="left:393px">Tarvo</div>
<div class="abs partner" style="left:625px">VKD</div>
<div class="abs partner" style="left:857px">Denholm</div>
<div class="abs center dots" style="top:3893px"><i></i><i class="on"></i><i></i></div>

<!-- FOOTER -->
<footer class="abs footer">
  <div class="fcol" style="left:160px">
    <h4>QUICK LINKS</h4>
    <ul><li>Home</li><li>About Us</li><li>Our Services</li><li>Prospora &amp; QA Technology</li><li>Intent Data</li><li>Testimonials</li><li>Contact Us</li></ul>
  </div>
  <div class="fcol" style="left:366px">
    <h4>CAREERS</h4>
    <div class="fsmall">Join our team of experts, curious<br>and ambitious</div>
    <div class="fred">EXPLORE OPENINGS →</div>
    <h4 class="subscribe" style="margin-bottom:0">SUBSCRIBE</h4>
    <div class="email-box"><span>Enter your email *</span><b>SEND →</b></div>
  </div>
  <div class="fcol company" style="left:675px">
    <h4>COMPANY</h4>
    <ul><li>Awards</li><li>Site Map</li><li>Terms &amp; Conditions</li><li>Support Services</li><li>Privacy Policy</li><li>Help</li><li>Support Services</li><li>Privacy Policy</li><li>Help</li></ul>
  </div>
  <div class="fcol contact" style="left:884px">
    <h4>CONTACT</h4>
    <ul>
      <li><svg viewBox="0 0 12 12"><path d="M6 1a3.5 3.5 0 0 1 3.5 3.5C9.5 7 6 11 6 11S2.5 7 2.5 4.5A3.5 3.5 0 0 1 6 1z" fill="#e0474d"/></svg>14 Carden Row Suite 210</li>
      <li><svg viewBox="0 0 12 12"><path d="M3 1l2 2.5-1.2 1.2a7 7 0 0 0 3.5 3.5L8.5 7 11 9l-1.5 2C5 11 1 7 1 2.5z" fill="#e0474d"/></svg>+44 20 7946 0321</li>
      <li><svg viewBox="0 0 12 12"><rect x="1" y="2.5" width="10" height="7" fill="none" stroke="#e0474d" stroke-width="1.2"/><path d="M1 3l5 3.5L11 3" fill="none" stroke="#e0474d" stroke-width="1.2"/></svg>contact@ledgerwisereach.example</li>
      <li><svg viewBox="0 0 12 12"><circle cx="6" cy="6" r="5" fill="none" stroke="#e0474d" stroke-width="1.2"/><path d="M6 3v3l2 1.5" fill="none" stroke="#e0474d" stroke-width="1.2"/></svg>From 07:05AM to 19:30PM</li>
    </ul>
  </div>
  <div class="abs copy">Ledgerwise Reach © 2020. All Rights Reserved</div>
  <div class="abs social"><i></i><i class="r"></i><i></i></div>
</footer>

</body>
</html>
```